Website re-design

We are a successful furnished apartment provider in Boston. We currently are working on re-designing our website www.bexlodging.com to make it more modern, designer look and user friendly. We hired a designer, but are not happy with the designs proposed and want to improve on them. The winning design will be paid regardless of whether we stay with our current designer or not. We want ideas and functional page links to see how it will work. Platform we have chosen is wordpress. Feel free to propose others easy for us to update and modify. We do not like Joomla on which website is currently running. We do not like flash nor long load times.
Please use photos on our website for design presentations. www.bexlodging.com

Target Market(s)

doctors, nurses, business men but mostly business women, some post-medical students

Industry/Entity Type

Apartment

Requirements
Must have
• Quick action button for reservation form and a notification and email forwarding system to us of reservation information by potential clients. Blog required with feedback by guests allowed, we can censor which are published. Slide shows of apartments.
Should not have
• No movies.

```html
<!DOCTYPE html>
<html lang="en">
<head>
<meta charset="utf-8">
<title>Bex Lodging – Furnished Apartments</title>
<link rel="stylesheet" href="https://fonts.googleapis.com/css2?family=Cinzel:wght@400;700&family=Open+Sans:wght@400&display=swap">
<style>
  :root {
    --bg-top: #cbbf86;
    --bg-bottom: #ece7d6;
    --header-black: #0b0a09;
    --gold: #cdb064;
    --gold-soft: #b89c57;
    --brown-heading: #6a5a30;
    --body-text: #6e6552;
    --footer-text: #a89c7c;
    --panel-white: #ffffff;
    --thumb-border: #d9d4c6;
    --icon-grey: #4a4a4a;
  }
  * { margin: 0; padding: 0; box-sizing: border-box; }
  html, body { width: 1200px; height: 1001px; overflow: hidden; }
  body {
    background: linear-gradient(180deg, var(--bg-top) 0%, #dcd3aa 45%, var(--bg-bottom) 100%);
    font-family: "Open Sans", sans-serif;
    position: relative;
  }
  .site-header {
    position: absolute; left: 240px; top: 53px; width: 720px; height: 98px;
    background: var(--header-black);
  }
  .brand { position: absolute; left: 34px; top: 25px; display: flex; align-items: center; gap: 10px; }
  .brand-mark { width: 46px; height: 46px; border-radius: 50%; background: var(--gold-soft); }
  .brand-name { font-family: "Cinzel", serif; color: var(--gold); font-size: 21px; letter-spacing: 1px; line-height: 1; }
  .brand-tagline { font-family: "Cinzel", serif; color: var(--gold); font-size: 7px; letter-spacing: 2.3px; margin-top: 4px; }
  .utility-nav { position: absolute; left: 336px; top: 52px; display: flex; gap: 15px; }
  .utility-nav a { font-family: "Cinzel", serif; color: var(--gold); font-size: 10.5px; text-decoration: none; }
  .social { position: absolute; left: 634px; top: 52px; display: flex; gap: 7px; }
  .social span { width: 12px; height: 12px; background: var(--icon-grey); display: block; }

  .hero {
    position: absolute; left: 240px; top: 151px; width: 720px; height: 367px;
    background: linear-gradient(100deg, #3b2414 0%, #8a5a2c 18%, #e8b36a 38%, #f3c98a 52%, #d89548 70%, #6b3e1c 88%, #2e1c10 100%);
    overflow: hidden;
  }
  .hero-photo { position: absolute; inset: 0; }
  .main-nav {
    position: absolute; left: 0; top: 0; width: 100%; height: 41px;
    background: rgba(70, 60, 45, 0.6);
  }
  .main-nav a {
    position: absolute; top: 12px; transform: translateX(-50%);
    font-family: "Cinzel", serif; color: var(--gold); font-size: 13.5px; text-decoration: none; white-space: nowrap;
  }
  .hero-caption {
    position: absolute; left: 0; bottom: 0; width: 100%; height: 125px;
    background: rgba(40, 25, 15, 0.5); text-align: center;
  }
  .hero-title { font-family: "Cinzel", serif; color: var(--gold); font-size: 24px; line-height: 26px; margin-top: 17px; font-weight: 400; }
  .hero-sub { font-family: "Cinzel", serif; color: var(--gold-soft); font-size: 10.5px; line-height: 16px; margin-top: 8px; letter-spacing: 0.5px; }

  .feature-panel {
    position: absolute; left: 247px; top: 518px; width: 705px; height: 157px;
    background: var(--panel-white);
    box-shadow: inset 0 6px 6px -4px rgba(0,0,0,0.35);
  }
  .feature-card {
    position: absolute; top: 19px; width: 159px; height: 116px;
    border: 1px solid var(--thumb-border); padding: 3px; background: var(--panel-white);
  }
  .feature-image { width: 100%; height: 100%; position: relative; }
  .feature-label {
    position: absolute; left: 0; bottom: 0; width: 100%; height: 41px;
    background: rgba(30, 20, 12, 0.55);
    font-family: "Cinzel", serif; color: var(--gold); font-size: 13px; text-align: center; line-height: 41px;
  }

  .intro { position: absolute; left: 417px; top: 706px; width: 340px; text-align: center; }
  .intro-title {
    font-family: "Cinzel", serif; color: var(--brown-heading); font-size: 26px; line-height: 26px; font-weight: 400;
    white-space: nowrap; margin: 0 -60px;
  }
  .intro-text { margin-top: 24px; text-align: justify; color: var(--body-text); font-size: 8.9px; line-height: 15.7px; letter-spacing: -0.1px; }
  .intro-sign { margin-top: 16px; font-family: "Cinzel", serif; color: var(--brown-heading); font-size: 11px; letter-spacing: 0.5px; }

  .site-footer {
    position: absolute; left: 0; top: 948px; width: 1200px; text-align: center;
    font-family: "Cinzel", serif; color: var(--footer-text); font-size: 9px;
  }
</style>
</head>
<body>
  <header class="site-header">
    <div class="brand">
      <span class="brand-mark"></span>
      <div>
        <div class="brand-name">Bex Lodging</div>
        <div class="brand-tagline">FURNISHED APARTMENTS</div>
      </div>
    </div>
    <nav class="utility-nav">
      <a href="#">Blog</a><a href="#">Updates</a><a href="#">Reviews</a><a href="#">Boston</a><a href="#">About Us</a>
    </nav>
    <div class="social"><span></span><span></span><span></span></div>
  </header>

  <section class="hero">
    <div class="hero-photo" role="img" aria-label="Sunlit furnished studio apartment with bed, dresser, windows and kitchenette"></div>
    <nav class="main-nav">
      <a href="#" style="left:104px">Contact</a>
      <a href="#" style="left:213px">Apartments</a>
      <a href="#" style="left:337px">Reservations</a>
      <a href="#" style="left:441px">Links</a>
      <a href="#" style="left:534px">Locations</a>
      <a href="#" style="left:629px">Rates</a>
    </nav>
    <div class="hero-caption">
      <h1 class="hero-title">Welcome to Bex Lodging<br>Furnished Apartments</h1>
      <p class="hero-sub">SHORT TERM AND EXTENDED STAY APARTMENTS<br>ARE VERY, VERY CLEAN.</p>
    </div>
  </section>

  <section class="feature-panel">
    <a class="feature-card" href="#" style="left:20px">
      <div class="feature-image" role="img" aria-label="Bright apartment bedroom" style="background:linear-gradient(90deg,#e9c58d,#d99a4e 50%,#7a4a22)">
        <span class="feature-label">Contact</span>
      </div>
    </a>
    <a class="feature-card" href="#" style="left:189px">
      <div class="feature-image" role="img" aria-label="Living room with fireplace and dining table" style="background:linear-gradient(90deg,#4a2c16,#c48a48 45%,#e6c9a0 75%,#6a4426)">
        <span class="feature-label">Apartments</span>
      </div>
    </a>
    <a class="feature-card" href="#" style="left:358px">
      <div class="feature-image" role="img" aria-label="Sitting room with red armchairs and tall windows" style="background:linear-gradient(90deg,#5a3a26,#e8dccb 45%,#c9b49a 60%,#4a2c1c)">
        <span class="feature-label">Reservations</span>
      </div>
    </a>
    <a class="feature-card" href="#" style="left:527px">
      <div class="feature-image" role="img" aria-label="Bright apartment bedroom" style="background:linear-gradient(90deg,#e9c58d,#d99a4e 50%,#7a4a22)">
        <span class="feature-label">Blog</span>
      </div>
    </a>
  </section>

  <main class="intro">
    <h2 class="intro-title">Welcome to Bex Lodging<br>Furnished Apartments</h2>
    <p class="intro-text">Bex Lodging is proud to offer some of the best furnished apartments in Boston. Our locations are in the trendiest area of the city: the South End. In the South End neighborhood, you will find wonderful restaurants, theaters, cafes and artist lofts. Our short term and extended stay apartments are very, very clean.</p>
    <p class="intro-sign">BEX LODGING TEAM</p>
  </main>

  <footer class="site-footer">© Bex Lodging 2012 - All Rights Reserved</footer>
</body>
</html>
```